Flyer für Installationsfirma für hochwertige Multimedia- und Beschallungslösungen, insbesonder in Kirchen und öffentlichen Bereichen mit Menschenansammlungen
Zielgruppe
Wir sind eine Installationsfirma für hochwertige Multimedia- und Beschallungslösungen in akustisch schwierigen Räumen. Im weiteren auch der Umbau auf LED Leuchten und dazugehörende Steuerungen. Unser Geschäft ist in Festinstallationen und Rentalbereich 'unterteilt' Weitere Infos auch auf www. alpen-ton.ch
Unser Zielpublikum sind die Festinstallation für Kirchen und öffentliche Räume. Mehrzweckräume, Bühnen, Kirchen, Aulas, Bahnhofshallen, Warteräume, Konferenzräume, Tagungszentren usw. Bei diesem Flyer sollen speziell die Kirchen beworben werden. Es ist wichtig dass nebst den oben beschriebenen Leistungen auch die Displaylösung für Liedanzeigen hervorgehoben wird.
Aufgabenstellung
Ansprechender Werbe-Flyer A4 2 Seitig
Spezifische Bilder und Texte zu den versch. Angebotsbereichen für Kirchen im Anhang. Vorschläge des Grafikers sind willkommen !
Die Texte und Bilder sollten von uns angepasst und korrigiert werden können !

```html
<!DOCTYPE html>
<html lang="de">
<head>
<meta charset="utf-8">
<title>Alpenton Flyer – Medieninstallation für Kirchenräume</title>
<link href="https://fonts.googleapis.com/css2?family=Poppins:wght@500;600;700&family=Open+Sans:wght@400;600;700&family=Roboto:wght@500&display=swap" rel="stylesheet">
<style>
  :root {
    --bg: #ebebed;
    --navy: #17213a;
    --navy-deep: #131b30;
    --band: #1b3655;
    --accent: #2a9fdb;
    --white: #ffffff;
    --text-soft: #c9d1df;
    --photo-violet: #8d6fc4;
    --photo-blue: #5c79b8;
    --photo-warm: #b59a7a;
  }
  * { box-sizing: border-box; margin: 0; padding: 0; }
  html, body { width: 909px; height: 1200px; overflow: hidden; background: var(--bg); }
  body { position: relative; font-family: "Open Sans", sans-serif; }

  .sheet {
    position: absolute; top: 296px; width: 430px; height: 608px;
    background: var(--navy); color: var(--white); overflow: hidden;
  }
  .sheet--front { left: 16px; }
  .sheet--back { left: 463px; }

  /* Front */
  .hero-photo {
    position: absolute; left: 0; top: 0; width: 100%; height: 300px;
    background:
      linear-gradient(180deg, rgba(23,33,58,0) 45%, var(--navy) 100%),
      radial-gradient(ellipse at 50% 55%, var(--photo-warm) 0%, rgba(181,154,122,0) 22%),
      linear-gradient(180deg, var(--photo-violet) 0%, var(--photo-blue) 55%, #3c4a78 100%);
  }
  .brand-mark {
    position: absolute; left: 36px; top: 40px; display: flex; align-items: center; gap: 7px;
    font-family: "Poppins", sans-serif; font-weight: 600; font-size: 13px; letter-spacing: 1px; color: var(--white);
  }
  .brand-mark .dot { width: 26px; height: 26px; border-radius: 50%; border: 3px solid var(--white); }

  .hero-title {
    position: absolute; top: 236px; left: 0; width: 100%; text-align: center;
    font-family: "Poppins", sans-serif; font-weight: 700; font-size: 25px; line-height: 32px;
    text-shadow: 0 0 18px rgba(42,159,219,.45);
  }
  .hero-title .accent { color: var(--accent); display: block; }
  .intro {
    position: absolute; top: 350px; left: 28px; width: 374px; text-align: center;
    font-size: 7.4px; line-height: 12.4px; color: var(--text-soft);
  }
  .features {
    position: absolute; top: 442px; left: 20px; width: 390px; display: flex; justify-content: space-between;
  }
  .feature { width: 92px; text-align: center; }
  .feature svg { width: 40px; height: 40px; display: block; margin: 0 auto 10px; }
  .feature-label { font-family: "Roboto", sans-serif; font-weight: 500; font-size: 12.5px; line-height: 16px; }

  .footer-band {
    position: absolute; left: 0; bottom: 0; width: 100%; height: 56px; background: var(--band);
    display: flex; align-items: center; padding-left: 34px;
  }
  .footer-name { font-family: "Open Sans", sans-serif; font-weight: 600; font-size: 20px; letter-spacing: 1px; width: 172px; }
  .footer-contact { font-size: 8.2px; font-weight: 700; line-height: 14.5px; }

  /* Back */
  .services-title {
    margin-top: 30px; text-align: center; font-family: "Poppins", sans-serif; font-weight: 700; font-size: 27px;
    text-shadow: 0 0 22px rgba(42,159,219,.5);
  }
  .services-title .accent { color: var(--accent); }
  .service { position: absolute; left: 26px; width: 390px; }
  .service-photo {
    position: absolute; width: 112px; height: 75px; border: 2px solid #e6e6e6;
  }
  .service-photo--warm { background: linear-gradient(135deg, #8a6a4a, #c9b08f 60%, #6d6658); }
  .service-photo--hall { background: radial-gradient(ellipse at 50% 60%, #d9b07a, #8a6540 70%, #5a4630); }
  .service-photo--rack { background: linear-gradient(160deg, #3a3f3a, #2a2d2b 50%, #4a3a32); }
  .service-photo--board { background: linear-gradient(170deg, #7d9860, #4a6040 60%, #5a5048); }
  .service-body { position: absolute; }
  .service-heading { font-family: "Poppins", sans-serif; font-weight: 600; font-size: 12px; margin-bottom: 5px; }
  .service-heading .accent { color: var(--accent); }
  .service-text { font-size: 7.4px; line-height: 12.3px; color: var(--text-soft); }

  .cta {
    position: absolute; left: 60px; top: 488px; width: 310px; height: 48px; border: 1.5px solid var(--accent);
    display: flex; align-items: center; justify-content: center; text-align: center;
    font-weight: 600; font-size: 10px; line-height: 15px; letter-spacing: .2px;
  }
</style>
</head>
<body>

<section class="sheet sheet--front">
  <div class="hero-photo" role="img" aria-label="Innenraum einer barocken Kirche mit violett-blauer Beleuchtung"></div>
  <div class="brand-mark"><span class="dot"></span>ALPENTON</div>

  <h1 class="hero-title">ZEITGEMÄSSE<br>MEDIENINSTALLATION<span class="accent">FÜR KIRCHENRÄUME</span></h1>

  <p class="intro">Multimediainstallation in Kirchen und Eventräumen. Für heutige Gottesdienste und multifunktionellen Betrieb von Gotteshäusern wird eine moderne Medientechnik benötigt. Beschallungssysteme mit sehr guter Sprachverständlichkeit durch Beam-Steering Technologie und dezenter Optik, LED-Beleuchtung und Projektion sind selbstverständlich geworden. Gleichzeitig gehört eine Integration der Heizung und Glockensteuerung zusammen mit der AV-Installation und einfache Bedienung via Tablet zum heutigen Anforderungsprofil einer Kirche.</p>

  <div class="features">
    <div class="feature">
      <svg viewBox="0 0 40 40" fill="none" stroke="#fff" stroke-width="1.6">
        <circle cx="20" cy="17" r="13"/><circle cx="20" cy="17" r="9"/>
        <path d="M12 28 L9 38 L14 35 L17 38 L18 30 M28 28 L31 38 L26 35 L23 38 L22 30"/>
        <text x="20" y="17" font-size="5.5" text-anchor="middle" fill="#fff" stroke="none" font-family="Open Sans, sans-serif" font-weight="700">25</text>
        <text x="20" y="22" font-size="3.5" text-anchor="middle" fill="#fff" stroke="none" font-family="Open Sans, sans-serif">Jahre</text>
      </svg>
      <div class="feature-label">25 Jahre<br>Erfahrung</div>
    </div>
    <div class="feature">
      <svg viewBox="0 0 40 40" fill="none" stroke="#fff" stroke-width="1.6">
        <circle cx="20" cy="16" r="13"/><circle cx="20" cy="16" r="8"/>
        <path d="M20 11.5 L21.5 14.6 L24.8 15 L22.4 17.3 L23 20.6 L20 19 L17 20.6 L17.6 17.3 L15.2 15 L18.5 14.6 Z"/>
        <path d="M12 26 L8 36 L13 34 L15 38 L19 29 M28 26 L32 36 L27 34 L25 38 L21 29"/>
      </svg>
      <div class="feature-label">Hochwertige<br>Ausrüstung</div>
    </div>
    <div class="feature">
      <svg viewBox="0 0 40 40" fill="none" stroke="#fff" stroke-width="1.6">
        <path d="M20 24 C12 18 12 11 16 10 C18 9.5 19.5 11 20 12.5 C20.5 11 22 9.5 24 10 C28 11 28 18 20 24 Z"/>
        <path d="M6 30 C10 28 14 28 18 30 L24 30 C26 30 26 33 24 33 L17 33 M6 35 C14 37 24 38 34 29"/>
        <path d="M20 2 V5 M10 5 L12 7 M30 5 L28 7 M6 14 H9 M31 14 H34"/>
      </svg>
      <div class="feature-label">Umfassender<br>Service</div>
    </div>
    <div class="feature">
      <svg viewBox="0 0 40 40" fill="none" stroke="#fff" stroke-width="1.6">
        <circle cx="20" cy="12" r="5"/><path d="M11 32 C11 22 29 22 29 32"/>
        <circle cx="9" cy="17" r="4"/><path d="M2 33 C2 25 14 25 14 28"/>
        <circle cx="31" cy="17" r="4"/><path d="M38 33 C38 25 26 25 26 28"/>
      </svg>
      <div class="feature-label">engagiertes<br>Team</div>
    </div>
  </div>

  <footer class="footer-band">
    <div class="footer-name">ALPENTON</div>
    <div class="footer-contact">Talstrasse 12 | 6430 Seewen | 041 555 20 20<br>mail@alpen-ton.ch | www.alpen-ton.ch</div>
  </footer>
</section>

<section class="sheet sheet--back">
  <h2 class="services-title">UNSERE <span class="accent">LEISTUNGEN</span></h2>

  <article class="service" style="top:88px;">
    <div class="service-photo service-photo--warm" style="left:0;top:0;" role="img" aria-label="Dezenter Säulenlautsprecher an einer Kirchenwand"></div>
    <div class="service-body" style="left:124px;top:0;width:268px;">
      <h3 class="service-heading"><span class="accent">BESCHALLUNG</span></h3>
      <p class="service-text">Die Anforderungen in akustisch schwierigen Räumen sind sehr hoch. Neuartige Beschallungskonzepte mit Beam-Steering Technologie machen eine hohe Sprachverständlichkeit in Kirchenräumen mit langer Nachhallzeit möglich. Zusammen mit einer normgerechten Installation einer Gehörlosenschlaufe können alle am Gottesdienst teilnehmen.</p>
    </div>
  </article>

  <article class="service" style="top:192px;">
    <div class="service-body" style="left:0;top:0;width:256px;">
      <h3 class="service-heading"><span class="accent">LED</span> BELEUCHTUNG</h3>
      <p class="service-text">Eine neue stromsparende Beleuchtung ist für einen verantwortungsvollen Energieeinsatz unumgänglich. Die stromsparenden LED-Leuchten sind durch die sehr lange Lebensdauer wartungsfrei und sehr kosteneffizient. Moderne LED-Leuchtmittel sind zudem flickerfrei, dimmbar und in der richtigen Farbtemperatur erhältlich.</p>
    </div>
    <div class="service-photo service-photo--hall" style="left:260px;top:0;" role="img" aria-label="Hell beleuchteter Kirchenraum mit Gemeinde"></div>
  </article>

  <article class="service" style="top:296px;">
    <div class="service-photo service-photo--rack" style="left:0;top:0;" role="img" aria-label="Steuerungsgeräte im Technikrack"></div>
    <div class="service-body" style="left:124px;top:0;width:268px;">
      <h3 class="service-heading"><span class="accent">INTERGRATION</span>/STEUERUNG</h3>
      <p class="service-text">Beleuchtung, Beschallung, Projektion, Liedanzeige, Glockensteuerung und Friedhofsbeleuchtung. Viele Systeme zusammengeführt in eine übersichtliche und erweiterbare Steuerung über Netzwerk.</p>
    </div>
  </article>

  <article class="service" style="top:394px;">
    <div class="service-body" style="left:0;top:0;width:256px;">
      <h3 class="service-heading"><span class="accent">LIEDER</span>/TEXTANZEIGEN</h3>
      <p class="service-text">Kostengünstige Liedanzeigen mit 8 Zeilen in allen Farbkombinationen. Auch Bilder können angezeigt werden (z.B. für Beerdigungen /Hochzeiten/Taufen usw).</p>
    </div>
    <div class="service-photo service-photo--board" style="left:260px;top:0;" role="img" aria-label="Elektronische Liedanzeige an der Kirchenwand"></div>
  </article>

  <div class="cta">KONTAKTIEREN SIE UNS UNVERBINDLICH FÜR EIN<br>PERSÖNLICHES BERATUNGSGESPRÄCH.</div>

  <footer class="footer-band">
    <div class="footer-name">ALPENTON</div>
    <div class="footer-contact">Talstrasse 12 | 6430 Seewen | 041 555 20 20<br>mail@alpen-ton.ch | www.alpen-ton.ch</div>
  </footer>
</section>

</body>
</html>
```